New Business Card Design Project

We would like a business card that represents the sale of boat, home, auto, and life insurance.

The logo can change colors to meet the look of the design if needed.

Industry/Entity Type

Business

```html
<!DOCTYPE html>
<html lang="en">
<head>
<meta charset="utf-8">
<title>Harborline Financial – Business Card</title>
<link rel="stylesheet" href="https://fonts.googleapis.com/css2?family=Lato:wght@400;700;900&display=swap">
<style>
  :root {
    --canvas-bg: #2b2b2b;
    --card-blue: #3f7792;
    --card-blue-light: #4d89a6;
    --card-white: #f7f7f7;
    --ink-dark: #2f3b44;
    --ink-black: #1d1d1d;
    --accent-blue: #2e6882;
    --divider-light: rgba(255, 255, 255, 0.75);
  }
  * { box-sizing: border-box; margin: 0; padding: 0; }
  html, body {
    width: 1200px;
    height: 997px;
    overflow: hidden;
    background: var(--canvas-bg);
    font-family: "Lato", Arial, sans-serif;
  }
  .canvas {
    position: relative;
    width: 1200px;
    height: 997px;
  }
  .card {
    position: absolute;
    left: 240px;
    width: 720px;
    height: 411px;
    box-shadow: 0 12px 30px rgba(0, 0, 0, 0.45);
  }

  /* ---------- Front: blue services card ---------- */
  .card--front {
    top: 52px;
    background: linear-gradient(135deg, var(--card-blue-light), var(--card-blue));
  }
  .card--front .brand {
    position: absolute;
    top: 118px;
    left: 0;
    width: 100%;
    display: flex;
    align-items: center;
    justify-content: center;
    gap: 16px;
  }
  .brand__mark {
    width: 22px;
    height: 22px;
    border-radius: 50%;
    background: var(--ink-dark);
  }
  .brand__name {
    font-weight: 400;
    font-size: 40px;
    letter-spacing: 8px;
    color: var(--ink-dark);
  }
  .services {
    position: absolute;
    left: 0;
    bottom: 60px;
    width: 100%;
    display: flex;
    justify-content: center;
    align-items: center;
    list-style: none;
  }
  .services__item {
    font-size: 15px;
    letter-spacing: 5px;
    color: var(--ink-dark);
    padding: 0 26px;
  }
  .services__item + .services__item {
    border-left: 2px solid var(--divider-light);
  }

  /* ---------- Back: white contact card ---------- */
  .card--back {
    top: 533px;
    background: var(--card-white);
  }
  .card--back .brand {
    position: absolute;
    top: 56px;
    right: 48px;
    display: flex;
    align-items: center;
    gap: 12px;
  }
  .card--back .brand__mark {
    width: 16px;
    height: 16px;
  }
  .card--back .brand__name {
    font-size: 28px;
    letter-spacing: 5px;
  }
  .rule {
    position: absolute;
    top: 160px;
    left: 200px;
    right: 48px;
    height: 3px;
    background: var(--accent-blue);
  }
  .person {
    position: absolute;
    top: 140px;
    left: 48px;
  }
  .person__name {
    font-weight: 900;
    font-size: 24px;
    color: var(--accent-blue);
    letter-spacing: 0.5px;
  }
  .person__role {
    font-weight: 900;
    font-size: 16px;
    color: var(--ink-black);
    margin-top: 2px;
  }
  .contacts {
    position: absolute;
    left: 48px;
    top: 236px;
    list-style: none;
  }
  .contacts__item {
    display: flex;
    align-items: center;
    gap: 14px;
    font-size: 17px;
    font-weight: 700;
    color: #333;
    height: 31px;
  }
  .contacts__icon {
    width: 18px;
    height: 18px;
    fill: var(--accent-blue);
  }
  .address {
    position: absolute;
    right: 48px;
    top: 236px;
    font-style: normal;
    font-weight: 900;
    font-size: 16px;
    line-height: 1.45;
    color: var(--ink-black);
    text-align: left;
  }
</style>
</head>
<body>
<main class="canvas">

  <section class="card card--front" aria-label="Business card front">
    <div class="brand">
      <span class="brand__mark"></span>
      <span class="brand__name">HARBORLINE FINANCIAL</span>
    </div>
    <ul class="services">
      <li class="services__item">BOAT</li>
      <li class="services__item">HOME</li>
      <li class="services__item">AUTO</li>
      <li class="services__item">LIFE INSURANCE</li>
    </ul>
  </section>

  <section class="card card--back" aria-label="Business card back">
    <div class="brand">
      <span class="brand__mark"></span>
      <span class="brand__name">HARBORLINE FINANCIAL</span>
    </div>
    <div class="rule"></div>

    <div class="person">
      <p class="person__name">YOUR NAME</p>
      <p class="person__role">DIRECTOR</p>
    </div>

    <ul class="contacts">
      <li class="contacts__item">
        <svg class="contacts__icon" viewBox="0 0 20 20" aria-hidden="true"><path d="M2 8c0-3 3-5 8-5s8 2 8 5l-1 2-4-1V7H7v2l-4 1zM5 11h10l2 6H3z"/></svg>
        0049 163 5550127
      </li>
      <li class="contacts__item">
        <svg class="contacts__icon" viewBox="0 0 20 20" aria-hidden="true"><path d="M5 2h10v5H5zM2 8h16v7h-3v-3H5v3H2zM6 13h8v5H6z"/></svg>
        0049 163 5550128
      </li>
      <li class="contacts__item">
        <svg class="contacts__icon" viewBox="0 0 20 20" aria-hidden="true"><path d="M2 4h16v12H2zM3.5 5.5 10 11l6.5-5.5v1.6L10 12.6 3.5 7.1z" fill-rule="evenodd"/></svg>
        info@harborlinefinancial.com
      </li>
      <li class="contacts__item">
        <svg class="contacts__icon" viewBox="0 0 20 20" aria-hidden="true"><path d="M8 12 12 8M7 9l-3 3a2.5 2.5 0 0 0 4 4l3-3M13 11l3-3a2.5 2.5 0 0 0-4-4L9 7" fill="none" stroke="#2e6882" stroke-width="2" stroke-linecap="round"/></svg>
        www.harborlinefinancial.com
      </li>
    </ul>

    <address class="address">
      2280 Tidewater Avenue,<br>
      Port Merrow, Florida 33990
    </address>
  </section>

</main>
</body>
</html>
```